Brochure 11 x 25.5 Trifold

Harborline Staffing Works, Inc. is a payroll, benefits, and HR administration company. We are in need of a brochure to showcase all of our services. Attached is a one-page information sheet that contains the information we want in the brochure as well as several images. The brochure is a 11 x 25.5 tri-fold (a sample is attached). Please use the colors in the attached logo and design to complement our website harborlineworks.example.
Target Market(s)
Company executives
Industry/Entity Type
Human Resource Management
Other font styles liked:
- Avenir LT

```html
<!DOCTYPE html>
<html lang="en">
<head>
<meta charset="utf-8">
<title>Harborline Staffing Works – Trifold Brochure</title>
<link rel="stylesheet" href="https://fonts.googleapis.com/css2?family=Nunito+Sans:wght@400;600;700;800;900&display=swap">
<style>
  :root{
    --navy:#0d3b61;
    --navy-deep:#0a2f4f;
    --green:#8db43b;
    --green-light:#a6c75a;
    --sky:#4ea9ea;
    --white:#ffffff;
    --stage:#2a2a2a;
    --ink-soft:#dfe8ef;
  }
  *{box-sizing:border-box;margin:0;padding:0}
  html,body{width:1200px;height:693px;overflow:hidden;background:var(--stage)}
  body{font-family:"Nunito Sans",Arial,sans-serif;color:var(--navy);position:relative}
  .panel{position:absolute;left:248px;width:728px;background:var(--white);overflow:hidden}
  .panel--outside{top:25px;height:312px}
  .panel--inside{top:356px;height:314px}
  .abs{position:absolute}
  svg.shapes{position:absolute;left:0;top:0}

  /* outside */
  .apart-title{left:11px;top:7px;font-size:14.5px;font-weight:800;color:var(--navy)}
  .focus-title{left:251px;top:11px;font-size:14.5px;font-weight:900;color:var(--navy);line-height:1}
  .focus-sub{left:251px;top:28px;font-size:11.8px;font-weight:600;color:var(--white);line-height:1}
  .feature{position:absolute;left:10px;width:230px;display:flex;align-items:center;gap:8px}
  .feature-icon{width:27px;height:27px;border-radius:50%;border:2px solid var(--green);background:var(--navy);flex:none;display:flex;align-items:center;justify-content:center}
  .feature-text{font-size:5.4px;line-height:6.6px;color:var(--white);width:195px}
  .hl{color:var(--green-light);font-weight:700}
  .contact{left:340px;width:120px;text-align:center;font-size:7px;font-weight:700;color:var(--navy);line-height:8.4px}
  .contact-dot{position:absolute;width:16px;height:16px;border-radius:50%;background:var(--green);left:392px}
  .social{position:absolute;top:204px;width:16px;height:16px;border-radius:50%;border:1.6px solid var(--green)}
  .brand{display:flex;align-items:center;gap:4px;font-weight:700;color:var(--navy);white-space:nowrap}
  .brand-dot{border-radius:50%;background:var(--green);flex:none}
  .phone-big{left:43px;top:291px;font-size:15px;font-weight:800;color:var(--navy)}
  .web{font-size:8.6px;font-weight:800;color:var(--white);display:flex;align-items:center;gap:4px}
  .web--dark{color:var(--navy)}
  .globe{width:9px;height:9px;border-radius:50%;border:1.4px solid var(--green);flex:none}
  .promise{left:494px;top:208px;width:212px;height:81px;text-align:center;color:var(--white)}
  .promise-line{font-size:12px;line-height:14px}
  .promise-line b{font-weight:900}
  .promise-big{font-size:19px;font-weight:600;color:var(--green);line-height:22px;margin-top:2px}
  .promise-big b{font-weight:900}

  /* inside */
  .hire-title{left:186px;top:3px;font-size:19px;font-weight:900;color:var(--white);line-height:24px}
  .hire-copy{left:186px;top:28px;width:378px;font-size:5.2px;line-height:6.5px;color:var(--white);font-weight:600}
  .services-title{left:5px;top:69px;font-size:17px;font-weight:800;color:var(--green)}
  .services-list{left:118px;top:70px;width:118px;text-align:right;color:var(--white);font-size:4.6px;line-height:5.55px}
  .svc-head{font-weight:800;color:var(--sky);font-size:5px;margin-top:4px}
  .svc-head:first-child{margin-top:0;color:var(--green)}
  .svc-head.green{color:var(--green)}
  .svc-head.white{color:var(--white)}
  .detail-list{left:490px;top:71px;width:118px;color:var(--navy);font-size:4.6px;line-height:5.7px}
  .detail-head{font-weight:800;font-size:5.6px;line-height:6.4px;margin-top:5px}
  .detail-head:first-child{margin-top:0}
  .detail-head.green{color:var(--green)}
  .detail-head.blue{color:var(--sky)}
  .wheel-label{position:absolute;font-size:4.6px;font-weight:800;text-align:center;line-height:5.4px;transform:translateX(-50%);white-space:nowrap}
  .wheel-label.navy{color:var(--navy)}
  .wheel-label.green{color:var(--green)}
  .wheel-label.blue{color:var(--sky)}
</style>
</head>
<body>

<!-- OUTSIDE SPREAD -->
<section class="panel panel--outside">
  <svg class="shapes" width="728" height="312" viewBox="0 0 728 312">
    <defs>
      <linearGradient id="teamTint" x1="0" y1="0" x2="1" y2="1">
        <stop offset="0" stop-color="#0f4a76"/>
        <stop offset="0.55" stop-color="#15557f"/>
        <stop offset="1" stop-color="#0c3a60"/>
      </linearGradient>
      <linearGradient id="officeLight" x1="0" y1="0" x2="1" y2="1">
        <stop offset="0" stop-color="#eaf2f8"/>
        <stop offset="0.6" stop-color="#c9d8e6"/>
        <stop offset="1" stop-color="#5f7a98"/>
      </linearGradient>
    </defs>
    <path d="M205 0 H475 C462 40 440 58 400 62 H240 C225 50 215 30 205 0 Z" fill="var(--green)"/>
    <path d="M240 62 H400 C440 58 462 40 475 0 H478 C466 44 444 64 400 66 H248 Z" fill="var(--navy)"/>
    <path role="img" aria-label="Photo of an office team meeting, tinted navy" d="M0 36 H330 C345 36 352 42 348 52 L258 250 C248 272 232 280 210 280 H0 Z" fill="url(#teamTint)"/>
    <path d="M348 52 L258 250 C248 272 232 280 210 280 L205 284 C238 284 254 276 264 252 L356 40 Z" fill="var(--green)"/>
    <path d="M0 286 H148 C160 288 166 300 168 312 H164 C160 298 154 290 146 290 H0 Z" fill="var(--green)"/>
    <path d="M246 312 C248 296 256 288 272 288 H510 C520 288 526 296 530 312 Z" fill="var(--navy)"/>
    <path d="M240 312 C244 290 254 284 272 284 H516 C526 284 533 294 536 312 H530 C526 296 520 288 510 288 H272 C256 288 248 296 246 312 Z" fill="var(--green)"/>
    <rect role="img" aria-label="Photo of three smiling colleagues reviewing work on a laptop" x="487" y="32" width="241" height="176" fill="url(#officeLight)"/>
    <path d="M494 236 C494 218 506 208 524 208 H680 C696 208 706 218 706 232 V272 C706 282 698 289 688 289 H494 Z" fill="var(--navy)"/>
    <path d="M706 289 L728 200 V312 H690 Z" fill="var(--green)"/>
    <path d="M530 312 C536 296 546 292 560 292 H700 L690 312 Z" fill="var(--white)"/>
    <path d="M530 312 C536 292 546 288 560 288 H702 L700 292 H560 C548 292 540 298 536 312 Z" fill="var(--green)"/>
  </svg>

  <div class="abs apart-title">What Sets Us Apart:</div>
  <div class="abs focus-title">SAVE TIME &amp; STAY FOCUSED</div>
  <div class="abs focus-sub">ON RUNNING YOUR BUSINESS</div>

  <div class="feature" style="top:46px">
    <div class="feature-icon"><svg width="14" height="12" viewBox="0 0 14 12"><g fill="#fff"><circle cx="3" cy="2" r="1.4"/><circle cx="7" cy="2" r="1.4"/><circle cx="11" cy="2" r="1.4"/><rect x="1.8" y="4" width="2.4" height="7"/><rect x="5.8" y="4" width="2.4" height="7"/><rect x="9.8" y="4" width="2.4" height="7"/></g></svg></div>
    <div class="feature-text">Our <span class="hl">dedicated team of experts</span> is always just a call or email away!<br>You get direct phone numbers to the professionals you need!</div>
  </div>
  <div class="feature" style="top:85px">
    <div class="feature-icon"><svg width="14" height="11" viewBox="0 0 14 11"><path d="M7 1 L13 4 L7 7 L1 4 Z" fill="#fff"/><path d="M3.5 5.5 V8.5 C5 10 9 10 10.5 8.5 V5.5 L7 7.2 Z" fill="#fff"/></svg></div>
    <div class="feature-text">We are equipped with <span class="hl">education, experience, certifications, and motivation.</span><br>Our staff executes at the highest level in payroll and HR every day.</div>
  </div>
  <div class="feature" style="top:127px">
    <div class="feature-icon"><svg width="14" height="13" viewBox="0 0 14 13"><g fill="none" stroke="#fff" stroke-width="1.3"><circle cx="3.5" cy="6.5" r="2"/><circle cx="11" cy="2.5" r="1.6"/><circle cx="11" cy="10.5" r="1.6"/><path d="M5.3 5.6 L9.5 3.2 M5.3 7.4 L9.5 9.8"/></g></svg></div>
    <div class="feature-text">Employee information is automatically integrated across all modules,<br><span class="hl">eliminating duplicate data entry and significantly reducing errors.</span></div>
  </div>
  <div class="feature" style="top:168px">
    <div class="feature-icon"><svg width="15" height="12" viewBox="0 0 15 12"><g fill="none" stroke="#fff" stroke-width="1.2"><rect x="1" y="1" width="9" height="7"/><path d="M4 11 H7 M5.5 8 V11"/><rect x="11.5" y="1" width="2.5" height="10"/></g></svg></div>
    <div class="feature-text">Our <span class="hl">advanced software</span> is used to process payroll for over 88,000 companies and 2.2 million employees nation-wide. It makes even the most complex payrolls easy.</div>
  </div>
  <div class="feature" style="top:208px">
    <div class="feature-icon"><svg width="11" height="14" viewBox="0 0 11 14"><g fill="none" stroke="#fff" stroke-width="1.2"><path d="M1 1 H7 L10 4 V13 H1 Z"/><path d="M3 6 H8 M3 8 H8 M3 10 H8"/></g></svg></div>
    <div class="feature-text"><span class="hl">Access your employee information how you need it when you need it</span> with our quick-access reports and intuitive report writer. We even provide custom reports!</div>
  </div>
  <div class="feature" style="top:248px">
    <div class="feature-icon"><svg width="15" height="13" viewBox="0 0 15 13"><g fill="none" stroke="#fff" stroke-width="1.2"><path d="M4 7 C1 7 1 3 4 3.5 C5 0.5 10 0.5 10.5 3.5 C14 3.5 14 7 11 7"/><rect x="4.5" y="6" width="6" height="4.5"/><path d="M6.5 12 H8.5"/></g></svg></div>
    <div class="feature-text"><span class="hl">Our client branded, cloud-based Employee and Manager portals</span> allow your employees to access their payroll information quicker and more securely than ever before!</div>
  </div>

  <div class="contact-dot" style="top:87px"><svg width="16" height="16" viewBox="0 0 16 16"><path d="M5 4 L7 4 L7.6 6 L6.6 7 C7.2 8.4 8 9.2 9.2 9.8 L10 8.8 L12 9.4 V11.4 C8 11.6 4.6 8.4 5 4 Z" fill="#fff"/></svg></div>
  <div class="abs contact" style="top:104px">555-014-2200</div>
  <div class="contact-dot" style="top:121px"><svg width="16" height="16" viewBox="0 0 16 16"><g fill="none" stroke="#fff" stroke-width="1.1"><rect x="4" y="5" width="8" height="6"/><path d="M4 5 L8 8.4 L12 5"/></g></svg></div>
  <div class="abs contact" style="top:139px">info@harborlineworks.example</div>
  <div class="contact-dot" style="top:154px"><svg width="16" height="16" viewBox="0 0 16 16"><path d="M8 3.5 C10.3 3.5 11.4 5.2 11.4 6.8 C11.4 9 8 12.6 8 12.6 C8 12.6 4.6 9 4.6 6.8 C4.6 5.2 5.7 3.5 8 3.5 Z" fill="#fff"/><circle cx="8" cy="6.8" r="1.3" fill="var(--green)"/></svg></div>
  <div class="abs contact" style="top:172px">1420 Quayside Drive<br>Riverton,<br>LA 70000</div>
  <div class="social" style="left:382px"></div>
  <div class="social" style="left:401px"></div>

  <div class="abs brand" style="left:322px;top:262px;font-size:10.5px"><span class="brand-dot" style="width:12px;height:12px"></span>Harborline Staffing Works</div>

  <div class="abs phone-big">555-014-2200</div>
  <div class="abs web" style="left:307px;top:294px"><span class="globe"></span>harborlineworks.example</div>

  <div class="abs brand" style="left:580px;top:22px;font-size:10px"><span class="brand-dot" style="width:12px;height:12px"></span>Harborline Staffing Works</div>

  <div class="abs promise" style="padding-top:11px">
    <div class="promise-line">YOUR <b>SINGLE-SOURCE</b></div>
    <div class="promise-line"><b>SOLUTION</b> FOR THE</div>
    <div class="promise-big">ENTIRE <b>EMPLOYEE</b></div>
  </div>
  <div class="abs web web--dark" style="left:560px;top:294px"><span class="globe"></span>harborlineworks.example</div>
</section>

<!-- INSIDE SPREAD -->
<section class="panel panel--inside">
  <svg class="shapes" width="728" height="314" viewBox="0 0 728 314">
    <defs>
      <linearGradient id="studyPhoto" x1="0" y1="0" x2="1" y2="1">
        <stop offset="0" stop-color="#e9eef3"/>
        <stop offset="0.5" stop-color="#c7b8a6"/>
        <stop offset="1" stop-color="#8a96a6"/>
      </linearGradient>
      <linearGradient id="handshakePhoto" x1="0" y1="0" x2="1" y2="1">
        <stop offset="0" stop-color="#e6ecf1"/>
        <stop offset="0.5" stop-color="#b79d85"/>
        <stop offset="1" stop-color="#3b4f68"/>
      </linearGradient>
    </defs>
    <!-- green header banner -->
    <path d="M160 0 H590 C582 30 572 48 550 52 H196 C180 52 168 32 160 0 Z" fill="var(--green)"/>
    <path d="M0 53 H550 C574 50 586 32 594 0 H598 C590 36 576 56 550 58 H0 Z" fill="var(--navy)"/>
    <rect x="0" y="60" width="243" height="254" fill="var(--navy)"/>
    <path d="M0 101 H84 C104 101 114 114 116 134 L126 314 H0 Z" fill="var(--sky)"/>
    <path role="img" aria-label="Photo of two women working together on a laptop" d="M0 106 H82 C98 106 107 117 109 134 L119 314 H0 Z" fill="url(#studyPhoto)"/>
    <path d="M598 0 H728 V198 H650 C628 198 614 186 610 164 Z" fill="var(--sky)"/>
    <path role="img" aria-label="Photo of a smiling woman shaking hands across a desk" d="M606 0 H728 V193 H652 C633 193 620 183 616 164 Z" fill="url(#handshakePhoto)"/>
    <g transform="translate(364 179)">
      <circle r="101" fill="#fff" stroke="var(--navy)" stroke-width="2"/>
      <circle r="46" fill="#fff" stroke="var(--navy)" stroke-width="2.5"/>
      <circle r="42" fill="none" stroke="var(--sky)" stroke-width="1"/>
      <g stroke="var(--navy)" stroke-width="1.6">
        <line x1="0" y1="-46" x2="0" y2="-101" transform="rotate(-20)"/>
        <line x1="0" y1="-46" x2="0" y2="-101" transform="rotate(20)"/>
        <line x1="0" y1="-46" x2="0" y2="-101" transform="rotate(60)"/>
        <line x1="0" y1="-46" x2="0" y2="-101" transform="rotate(100)"/>
        <line x1="0" y1="-46" x2="0" y2="-101" transform="rotate(140)"/>
        <line x1="0" y1="-46" x2="0" y2="-101" transform="rotate(180)"/>
        <line x1="0" y1="-46" x2="0" y2="-101" transform="rotate(220)"/>
        <line x1="0" y1="-46" x2="0" y2="-101" transform="rotate(260)"/>
        <line x1="0" y1="-46" x2="0" y2="-101" transform="rotate(300)"/>
      </g>
      <g>
        <path d="M-4 -112 L6 -107 L-4 -102 Z" fill="var(--green)" transform="rotate(10)"/>
        <path d="M-4 -112 L6 -107 L-4 -102 Z" fill="var(--sky)" transform="rotate(48)"/>
        <path d="M-4 -112 L6 -107 L-4 -102 Z" fill="var(--navy)" transform="rotate(88)"/>
        <path d="M-4 -112 L6 -107 L-4 -102 Z" fill="var(--green)" transform="rotate(130)"/>
        <path d="M-4 -112 L6 -107 L-4 -102 Z" fill="var(--sky)" transform="rotate(172)"/>
        <path d="M-4 -112 L6 -107 L-4 -102 Z" fill="var(--navy)" transform="rotate(212)"/>
        <path d="M-4 -112 L6 -107 L-4 -102 Z" fill="var(--green)" transform="rotate(252)"/>
        <path d="M-4 -112 L6 -107 L-4 -102 Z" fill="var(--sky)" transform="rotate(292)"/>
        <path d="M-4 -112 L6 -107 L-4 -102 Z" fill="var(--navy)" transform="rotate(330)"/>
      </g>
      <g fill="none" stroke="var(--sky)" stroke-width="1.3">
        <circle cx="2" cy="-87" r="7"/>
        <circle cx="48" cy="-72" r="7"/>
        <circle cx="80" cy="-22" r="7"/>
        <circle cx="68" cy="36" r="7"/>
        <circle cx="-26" cy="48" r="7"/>
        <circle cx="-50" cy="40" r="9"/>
        <circle cx="-82" cy="-22" r="7"/>
        <circle cx="-56" cy="-66" r="7"/>
      </g>
      <g fill="none" stroke="var(--navy)" stroke-width="1.3">
        <rect x="23" y="31" width="10" height="12"/>
        <path d="M25.5 35 H30.5 M25.5 38 H30.5"/>
      </g>
    </g>
    <path d="M275 314 C278 302 286 296 300 296 H420 C434 296 442 302 446 314 Z" fill="var(--navy)"/>
    <rect x="570" y="222" width="128" height="81" rx="3" fill="#1d1d1f"/>
    <rect role="img" aria-label="Payroll dashboard screen with charts" x="573" y="225" width="122" height="75" fill="#f4f7fa"/>
    <g>
      <rect x="573" y="225" width="122" height="4" fill="var(--navy)"/>
      <circle cx="605" cy="255" r="9" fill="var(--sky)"/>
      <path d="M605 255 L605 246 A9 9 0 0 1 614 255 Z" fill="#c0392b"/>
      <polyline points="630,262 640,258 650,256 660,250 670,246 680,238" fill="none" stroke="var(--sky)" stroke-width="1"/>
      <circle cx="648" cy="285" r="7" fill="var(--sky)"/>
      <path d="M648 285 L648 278 A7 7 0 0 1 655 285 Z" fill="#c0392b"/>
      <g stroke="#c9d3dd" stroke-width="0.6"><line x1="578" y1="276" x2="630" y2="276"/><line x1="578" y1="280" x2="630" y2="280"/><line x1="578" y1="284" x2="630" y2="284"/><line x1="578" y1="288" x2="630" y2="288"/></g>
    </g>
    <rect x="684" y="237" width="37" height="72" rx="5" fill="#e9ecef" stroke="#b8bfc7" stroke-width="0.8"/>
    <rect role="img" aria-label="Mobile employee portal screen" x="687" y="244" width="31" height="56" fill="#5a6f86"/>
  </svg>

  <div class="abs brand" style="left:10px;top:19px;font-size:10px"><span class="brand-dot" style="width:11px;height:11px"></span>Harborline Staffing Works</div>
  <div class="abs hire-title">From hire to retire,</div>
  <div class="abs hire-copy">Harborline Staffing Works has been delivering quality HR and Payroll services for over 25 years. Our dedicated team of professionals is focused on being the best service provider in the industry. Our goal is to relieve business executives of the challenges of managing a dynamic and growing workforce in today's regulatory environment and give them the freedom to focus on what drives their business.</div>

  <div class="abs services-title">Our services</div>
  <div class="abs services-list">
    <div class="svc-head">PAYROLL</div>
    <div>• Fast, efficient, accurate</div>
    <div>• Paper checks or direct deposit</div>
    <div>• Easy time file uploads or integrated time clock options</div>
    <div>• New hire reporting</div>
    <div>• Custom G/L file</div>
    <div>• Comprehensive reporting options</div>
    <div>• Certified payroll option</div>
    <div class="svc-head">BENEFITS MANAGEMENT</div>
    <div>• Customized benefits packet</div>
    <div>• Track new hire eligibility</div>
    <div>• Open enrollment assistance</div>
    <div>• Electronic enrollment</div>
    <div>• Track and submit enrollments</div>
    <div>• Provide 401k census report</div>
    <div>• Remit retirement plan reports and funds</div>
    <div>• ACA compliance</div>
    <div class="svc-head white">EMPLOYEE ONBOARDING</div>
    <div>• Simple, accurate, paperless</div>
    <div>• Custom forms and acknowledgements</div>
    <div>• Standard forms (W-4, I-9, State withholding, etc)</div>
    <div>• Paperless, electronic signatures</div>
    <div>• Employee handbook and policy acknowledgements</div>
    <div>• Custom welcome videos</div>
    <div class="svc-head green">COBRA ADMINISTRATION</div>
    <div>• Initial notices</div>
    <div>• Open enrollment notices</div>
    <div>• Easy 24/7 online reporting</div>
    <div>• Qualified beneficiary election notices</div>
    <div>• Premium collection</div>
    <div>• Access to professional advice</div>
    <div class="svc-head">COMPLIANCE</div>
    <div>• Certified experts ensure compliance</div>
    <div>with all labor laws and regulations</div>
    <div>• OSHA Reporting</div>
    <div>• Affirmative Action (EEOC)</div>
    <div>• Affordable Care Act (ACA)</div>
    <div>• Family Medical Leave Act (FMLA)</div>
    <div>• Workers' Comp audits</div>
  </div>

  <div class="wheel-label navy" style="left:317px;top:123px">CAFETARIA/FSA/HRA<br>ADMINISTRATION</div>
  <div class="wheel-label green" style="left:366px;top:119px">PAYROLL</div>
  <div class="wheel-label blue" style="left:409px;top:126px">BENEFITS<br>MANAGEMENT</div>
  <div class="wheel-label navy" style="left:438px;top:173px">EMPLOYEE<br>ONBOARDING</div>
  <div class="wheel-label green" style="left:428px;top:198px">COBRA<br>ADMINISTRATION</div>
  <div class="wheel-label blue" style="left:391px;top:252px">COMPLIANCE</div>
  <div class="wheel-label navy" style="left:340px;top:249px">HUMAN<br>RESOURCE<br>ADMINISTRATION</div>
  <div class="wheel-label green" style="left:302px;top:196px">TIME AND<br>ATTENDANCE</div>
  <div class="wheel-label blue" style="left:291px;top:170px">TALENT<br>ACQUISITION</div>
  <div class="abs brand" style="left:338px;top:174px;font-size:7px">Harborline</div>

  <div class="abs detail-list">
    <div class="detail-head">HUMAN RESOURCE ADMINISTRATION</div>
    <div>• Wage and hour compliance</div>
    <div>• Employee handbooks</div>
    <div>• Employee discipline and termination consulting</div>
    <div>• Performance management</div>
    <div>• Workers' comp claims administration</div>
    <div>• Unemployment administration</div>
    <div>• Manager training</div>
    <div class="detail-head green">TIME AND ATTENDANCE</div>
    <div>• Integrated with payroll (no double entry)</div>
    <div>• Mobile and geofencing options</div>
    <div>• Overtime notices</div>
    <div>• Online time-off requests</div>
    <div>• Swipe and proximity card clocks</div>
    <div>• Biometric clocks</div>
    <div>• PTO tracking</div>
    <div class="detail-head blue">TALENT ACQUISITION</div>
    <div>• Custom careers page</div>
    <div>• Standard or custom job applications</div>
    <div>• Easy conversion of applicant data to employee data</div>
    <div>• Review, rate, and contact applicants</div>
    <div>• Mobile-friendly access</div>
    <div>• Easy posting to top job<br>&nbsp;&nbsp;boards</div>
    <div>• Candidate screening</div>
    <div class="detail-head">CAFETERIA/FSA/HRA<br>ADMINISTRATION</div>
    <div>• Plan documents/materials</div>
    <div>• Debit cards</div>
    <div>• Easy 24/7 online reporting</div>
    <div>• Claims processing</div>
    <div>• Plan testing</div>
  </div>

  <div class="abs web" style="left:306px;top:299px"><span class="globe"></span>harborlineworks.example</div>
</section>

</body>
</html>
```